LOCAL TAXI SERVICE NEEDS A BANNER AD DESIGN

NEED BANNER AD DESIGN FOR TAXI SERVICE IN NJ. WE PROVIDE LOCAL AND LONG DISTANCE TRANSPORTATION. OUR MAIN BASE OF CUSTOMER GO TO THE MAJOR AIRPORTS IN THE TRI STATE AREA. I WANT TO OFFER A SPECIAL GOING TO HOLMBRIDGE AIRPORT OF $35.00 WITH A COUPON CODE OF PW 12. THIS BANNER AD WILL BE USED FOR MY PALWIRE PAGE

Target Market(s)

PEOPLE WHO TRAVEL A LOT

Industry/Entity Type

Taxi

Font styles to use
Serif
Sans Serif

Colors
0792cd
0255a3
33a6d7
85cae6
cee9f5
ecf7fb
ffffff

Requirements
Must have
• MY COMPANY NAME: DORVAN'S TAXI

```html
<!DOCTYPE html>
<html lang="en">
<head>
<meta charset="utf-8">
<title>Dorvan's Taxi – Airport Banner</title>
<link href="https://fonts.googleapis.com/css2?family=Open+Sans:wght@600;700&display=swap" rel="stylesheet">
<style>
  :root{
    --page:#eef1f4;
    --blue-deep:#0255a3;
    --blue-mid:#0792cd;
    --blue-bright:#33a6d7;
    --blue-soft:#85cae6;
    --blue-pale:#cee9f5;
    --white:#ffffff;
    --navy:#0c1a28;
    --navy-2:#13293d;
    --logo-band:#2b2b2b;
    --sky:#9aa1a8;
    --road:#55575a;
  }
  *{margin:0;padding:0;box-sizing:border-box}
  html,body{width:867px;height:1200px;overflow:hidden}
  body{
    background:var(--page);
    font-family:"Open Sans",Arial,sans-serif;
    position:relative;
  }
  .banner{
    position:absolute;left:33px;width:800px;height:417px;overflow:hidden;
    box-shadow:0 6px 18px rgba(0,0,0,.25);
  }
  .banner--light{top:43px;background:linear-gradient(135deg,var(--blue-bright) 0%,var(--blue-soft) 60%,var(--blue-pale) 100%)}
  .banner--dark{top:576px;background:linear-gradient(135deg,var(--navy-2) 0%,var(--navy) 100%)}
  .banner__scene{position:absolute;inset:0}
  .logo{
    position:absolute;left:0;top:17px;height:40px;width:196px;
    background:var(--logo-band);
    clip-path:polygon(0 0,100% 0,88% 100%,0 100%);
    display:flex;align-items:center;gap:8px;padding-left:12px;
  }
  .logo__mark{width:22px;height:22px;background:var(--blue-bright)}
  .logo__name{color:var(--white);font-weight:600;font-size:17px;letter-spacing:.5px}
  .headline{
    position:absolute;right:17px;top:22px;text-align:right;color:var(--white);font-weight:700;line-height:1.15;
  }
  .headline__lead{font-size:27px}
  .headline__place{font-size:32px}
  .headline__accent{color:var(--blue-deep)}
  .banner--dark .headline__accent{color:var(--blue-bright)}
  .offer{
    position:absolute;right:17px;top:168px;font-size:27px;font-weight:700;color:var(--white);
  }
  .offer__accent{color:var(--blue-deep)}
  .banner--dark .offer__accent{color:var(--blue-bright)}
  .price{
    position:absolute;right:0;top:213px;width:156px;height:67px;
    background:linear-gradient(180deg,var(--blue-mid),var(--blue-deep));
    color:var(--white);font-weight:700;font-size:35px;
    display:flex;align-items:center;justify-content:flex-end;padding-right:17px;
    box-shadow:-4px 4px 10px rgba(0,0,0,.25);
  }
  .coupon{
    position:absolute;right:0;top:290px;width:263px;height:105px;
    background:linear-gradient(180deg,var(--blue-mid),var(--blue-deep));
    color:var(--white);text-align:right;padding:14px 17px 0 0;
    box-shadow:-4px 4px 10px rgba(0,0,0,.25);
  }
  .coupon__label{font-size:18px;font-weight:600}
  .coupon__code{font-size:42px;font-weight:700;line-height:1.25}
</style>
</head>
<body>

<section class="banner banner--light">
  <svg class="banner__scene" width="800" height="417" viewBox="0 0 800 417">
    <defs>
      <linearGradient id="road-light" x1="0" y1="0" x2="0" y2="1">
        <stop offset="0" stop-color="#c9ced3"/>
        <stop offset=".45" stop-color="var(--sky)"/>
        <stop offset=".55" stop-color="#8a7d66"/>
        <stop offset="1" stop-color="var(--road)"/>
      </linearGradient>
      <linearGradient id="car-light" x1="0" y1="0" x2="0" y2="1">
        <stop offset="0" stop-color="#f4f5f6"/>
        <stop offset="1" stop-color="#c4c7ca"/>
      </linearGradient>
    </defs>
    <polygon points="0,0 467,0 253,417 0,417" fill="url(#road-light)" role="img" aria-label="Photo of an open country road under a cloudy sky"/>
    <rect x="107" y="195" width="400" height="195" rx="60" fill="url(#car-light)" role="img" aria-label="Photo of a white sedan taxi"/>
  </svg>
  <div class="logo"><span class="logo__mark"></span><span class="logo__name">DORVAN'S TAXI</span></div>
  <h2 class="headline">
    <span class="headline__lead">WANT TO GOING</span><br>
    <span class="headline__place">HOLMBRIDGE <span class="headline__accent">AIRPORT</span> ?</span>
  </h2>
  <p class="offer"><span class="offer__accent">SPECIAL OFFER</span> PRICE</p>
  <div class="price">$35.00</div>
  <div class="coupon">
    <p class="coupon__label">USE THIS COUPON CODE</p>
    <p class="coupon__code">PW12</p>
  </div>
</section>

<section class="banner banner--dark">
  <svg class="banner__scene" width="800" height="417" viewBox="0 0 800 417">
    <defs>
      <linearGradient id="road-dark" x1="0" y1="0" x2="0" y2="1">
        <stop offset="0" stop-color="#c9ced3"/>
        <stop offset=".45" stop-color="var(--sky)"/>
        <stop offset=".55" stop-color="#8a7d66"/>
        <stop offset="1" stop-color="var(--road)"/>
      </linearGradient>
      <linearGradient id="car-dark" x1="0" y1="0" x2="0" y2="1">
        <stop offset="0" stop-color="#f4f5f6"/>
        <stop offset="1" stop-color="#c4c7ca"/>
      </linearGradient>
    </defs>
    <polygon points="0,0 467,0 253,417 0,417" fill="url(#road-dark)" role="img" aria-label="Photo of an open country road under a cloudy sky"/>
    <rect x="107" y="195" width="400" height="195" rx="60" fill="url(#car-dark)" role="img" aria-label="Photo of a white sedan taxi"/>
  </svg>
  <div class="logo"><span class="logo__mark"></span><span class="logo__name">DORVAN'S TAXI</span></div>
  <h2 class="headline">
    <span class="headline__lead">WANT TO GOING</span><br>
    <span class="headline__place">HOLMBRIDGE <span class="headline__accent">AIRPORT</span> ?</span>
  </h2>
  <p class="offer"><span class="offer__accent">SPECIAL OFFER</span> PRICE</p>
  <div class="price">$35.00</div>
  <div class="coupon">
    <p class="coupon__label">USE THIS COUPON CODE</p>
    <p class="coupon__code">PW12</p>
  </div>
</section>

</body>
</html>
```